Design for an A4 product factsheet

We need a client facing factsheet to explain our products to new and existing clients. There are 10 products, each factsheet needs to have the identical style and layout with the only difference being the copy, we will provide all copy but require a consistent, creative, engaging and 'on brand' layout.

Target market is HR Directors, Compensation & Benefit Managers, Finance Directors and Company Owners

Target Market(s)

Small and Medium sized businesses in the UK with between 50 and 5000 staff

Industry/Entity Type

Product

Other font styles liked:
• Calibri

Requirements
Must have
• An on-brand style consistent with previous designs.
• Use of identical iconography to prior designs for each of our products. These are detailed on the attachments of previous work.
• Immediate impact to grab the attention of a busy professional individual.
• Use of the Vell logo
Nice to have
• Incorporation of our OQR Graphic image.
Should not have
• Any off brand colours

```html
<!DOCTYPE html>
<html lang="en">
<head>
<meta charset="utf-8">
<title>Group Income Protection – Vell factsheet</title>
<link href="https://fonts.googleapis.com/css2?family=Lato:wght@400;700&display=swap" rel="stylesheet">
<style>
  :root {
    --navy: #1f3b5e;
    --navy-deep: #1c3353;
    --navy-light: #2e5a8f;
    --body: #5d6c82;
    --rule: #9aa7b8;
    --avatar: #5fb6c8;
    --footer-soft: #c8d2de;
    --footer-text: #d9e1ea;
    --white: #ffffff;
  }
  * { box-sizing: border-box; margin: 0; padding: 0; }
  html, body { width: 848px; height: 1200px; overflow: hidden; background: var(--white); }
  body { font-family: "Lato", sans-serif; color: var(--body); }
  .sheet { position: relative; width: 848px; height: 1200px; overflow: hidden; }

  .hero-photo { position: absolute; top: 0; right: 0; width: 848px; height: 380px; }

  .brand { position: absolute; left: 52px; top: 62px; display: flex; align-items: center; gap: 9px; }
  .brand-mark { width: 12px; height: 12px; background: var(--navy); }
  .brand-name { font-size: 30px; color: var(--navy); font-weight: 400; line-height: 1; }

  .teaser { position: absolute; left: 172px; top: 48px; color: var(--navy); }
  .teaser-lead { font-size: 13px; }
  .teaser-main { font-size: 17px; font-weight: 700; margin-top: 4px; }
  .teaser-tail { font-size: 12px; margin: 4px 0 0 48px; }
  .teaser-tail b { font-size: 17px; }

  .product-frame { position: absolute; left: 77px; top: 168px; width: 643px; height: 67px;
    border-left: 1px solid var(--rule); border-bottom: 1px solid var(--rule); }
  .product-icon { position: absolute; left: 80px; top: 138px; width: 72px; }
  .product-icon span { display: block; font-size: 9.5px; color: var(--navy); text-align: center; line-height: 1.05; margin-top: 2px; }
  .product-title { position: absolute; left: 164px; top: 177px; font-size: 32px; font-weight: 700; color: var(--navy); letter-spacing: 0.3px; }

  .column { position: absolute; top: 296px; width: 298px; }
  .column.left { left: 102px; }
  .column.right { left: 448px; }
  .column h2 { font-size: 15.5px; font-weight: 400; color: var(--navy); margin-bottom: 19px; }
  .column p { font-size: 12px; line-height: 19.6px; text-align: justify; margin-bottom: 19px; }
  .column p + h2 { margin-top: 6px; }

  .pull-quote { position: absolute; left: 140px; top: 786px; color: var(--navy); }
  .pull-quote .mark { font-size: 48px; font-weight: 700; line-height: 0; vertical-align: -16px; margin-right: 10px; }
  .pull-quote .small { font-size: 23px; }
  .pull-quote .large { font-size: 35px; margin-left: 6px; }
  .pull-quote .large.second { font-size: 26px; }
  .pull-quote .line2 { margin: 6px 0 0 102px; }

  .fact-box { position: absolute; top: 919px; width: 178px; height: 144px; border-radius: 7px; overflow: hidden;
    background: linear-gradient(to top right, var(--navy-deep) 50%, var(--navy-light) 50%); color: var(--white); text-align: center; }
  .fact-box h3 { font-size: 13px; font-weight: 400; margin-top: 25px; letter-spacing: 0.3px; }
  .fact-box p { font-size: 10.5px; line-height: 15px; margin: 22px 14px 0; }
  .fact-box.employer { left: 130px; }
  .fact-box.employee { left: 333px; }
  .fact-box.cost { left: 539px; }

  .footer { position: absolute; left: 0; top: 1110px; width: 848px; height: 90px; background: var(--navy-deep); color: var(--white); }
  .footer-avatar { position: absolute; left: 42px; top: 24px; width: 34px; height: 40px; border-radius: 17px 17px 6px 6px; background: var(--avatar); }
  .footer-prompt { position: absolute; left: 94px; top: 30px; }
  .footer-prompt strong { font-size: 12.5px; display: block; }
  .footer-prompt span { font-size: 11px; color: var(--footer-soft); }
  .footer-contact { position: absolute; left: 352px; top: 27px; font-size: 14px; line-height: 20px; color: var(--footer-text); }
  .footer-contact b { color: var(--white); font-weight: 700; }
</style>
</head>
<body>
<div class="sheet">
  <svg class="hero-photo" viewBox="0 0 848 380" role="img" aria-label="Photo of a businessman in a chair sketching benefit icons on a chalkboard">
    <defs>
      <linearGradient id="heroTone" x1="0" y1="0" x2="1" y2="1">
        <stop offset="0" stop-color="#3a3f47"/>
        <stop offset="0.6" stop-color="#23272d"/>
        <stop offset="1" stop-color="#4a5058"/>
      </linearGradient>
    </defs>
    <polygon points="468,0 848,0 848,380" fill="url(#heroTone)"/>
  </svg>

  <div class="brand">
    <span class="brand-mark"></span>
    <span class="brand-name">Vell</span>
  </div>

  <div class="teaser">
    <p class="teaser-lead">Which</p>
    <p class="teaser-main">EMPLOYEE BENEFITS</p>
    <p class="teaser-tail">do you provide for your staff <b>?</b></p>
  </div>

  <div class="product-frame"></div>
  <div class="product-icon">
    <svg width="72" height="58" viewBox="0 0 72 58" fill="none" stroke="#1f3b5e" stroke-width="2">
      <path d="M30 10 L42 10 L38 17 L34 17 Z"/>
      <path d="M34 17 C22 22 22 40 36 40 C50 40 50 22 38 17"/>
      <text x="36" y="34" font-size="12" font-family="Lato, sans-serif" text-anchor="middle" fill="#1f3b5e" stroke="none" font-weight="700">£</text>
      <path d="M14 30 L14 44 C20 52 30 50 36 50 C42 50 52 52 58 44 L58 30"/>
    </svg>
    <span>Group Income Protection</span>
  </div>
  <h1 class="product-title">GROUP INCOME PROTECTION</h1>

  <section class="column left">
    <h2>What is Group Income Protection?</h2>
    <p>Group Income Protection, or Permanent Health Insurance, is designed to pay out a percentage of an employee’s salary if that employee is unable to work due to a long-term illness.</p>
    <h2>How does it work?</h2>
    <p>If an employee is absent from work due to illness or injury for a certain period then the insurance company pays a percentage of salary to the employer, who, in turn, pays the employee through PAYE.</p>
    <p>The length of time the employee has to be absent for is set by the employer as part of the policy, and can range from 13 weeks up to 52 weeks. The percentage of salary to be covered is also set by the employer, but is usually 50% or 66% of salary.</p>
    <p>The payments on the plan will continue until the employee returns to work or the policy term ends. Again, employers set the policy term and this can be a limited period of 5 or 10 years, or run until State Pension Age.</p>
  </section>

  <section class="column right">
    <h2>Why is it valuable?</h2>
    <p>Having a Group Income Protection policy means that an employer can continue to pay an employee a proportion of their salary whilst they are off long-term sick. Knowing that they still have a regular income that is well in excess of Statutory Sick Pay (£88.45 per week in 2016/17) is extremely positive for someone who is likely suffering from a serious illness or injury.</p>
    <p>It is not a P11d benefit for employees and, in most cases, the employee does not have to complete any medical forms before cover starts. This means people who may struggle to get cover individually can still benefit from the cover as long as they are working.</p>
    <h2>What does it cost?</h2>
    <p>The cost of cover depends on a number of factors. The profile of the workforce is important and then other factors, such as the amount of cover, the time which elapses before a claim starts, and the maximum period the claim would be paid for, are taken into account.</p>
  </section>

  <blockquote class="pull-quote">
    <p><span class="mark">“</span><span class="small">Lorem Ipsum</span> <span class="large">Sit Dolor Met</span></p>
    <p class="line2"><span class="small">consectetur adipiscing</span> <span class="large second">sed do eiusmod</span></p>
  </blockquote>

  <div class="fact-box employer">
    <h3>EMPLOYER TAX</h3>
    <p>Corporation Tax relief</p>
  </div>
  <div class="fact-box employee">
    <h3>EMPLOYEE TAX</h3>
    <p>No direct tax implications for employee. Income tax and NICs deducted from benefit paid through PAYE</p>
  </div>
  <div class="fact-box cost">
    <h3>COST TO EMPLOYER</h3>
    <p>1%- 2% of gross payroll, depending on cover. Can be less if payment term is limited</p>
  </div>

  <footer class="footer">
    <div class="footer-avatar" role="img" aria-label="Illustrated customer service adviser"></div>
    <div class="footer-prompt">
      <strong>Want to find out how we can help?</strong>
      <span>Why not get in touch?</span>
    </div>
    <p class="footer-contact">Call us today on <b>01632 960418</b>, visit us online at <b>www.thevellgroup.co.uk</b><br>or email <b>hello@thevellgroup.co.uk</b> to find out more.</p>
  </footer>
</div>
</body>
</html>
```